33.5 x 80 - Retractable Banner - Harbor Crest Realty Group

Harbor Crest Realty Group

A Full Service Real Estate Brokerage

Home of the LIFT PROGRAM
"A program that teaches, supports and celebrates Agents generating Multiple Streams of Income"

Licensed in DC, MD and VA

Phone (301) 555-0172
www.harborcrestrealty.example
www.careersatharborcrest.example
@harborcrestrealtygroup

```html
<!DOCTYPE html>
<html lang="en">
<head>
<meta charset="utf-8">
<title>Harbor Crest Realty Group – Retractable Banner</title>
<link rel="stylesheet" href="https://fonts.googleapis.com/css2?family=Poppins:wght@400;500;600;700&family=Montserrat:wght@500;700&display=swap">
<style>
  :root {
    --teal: #008b99;
    --white: #ffffff;
    --bg-light: #f4f5f6;
    --bg-mid: #e4e6e8;
    --photo-top: #c9ccd1;
    --photo-bottom: #1c1d22;
  }
  html, body { margin: 0; padding: 0; overflow: hidden; }
  body { width: 1200px; height: 2865px; }
  .banner {
    position: relative;
    width: 1200px;
    height: 2865px;
    overflow: hidden;
    background: linear-gradient(160deg, var(--bg-light) 0%, var(--bg-mid) 45%, var(--bg-light) 70%, var(--bg-mid) 100%);
    font-family: "Poppins", sans-serif;
    color: var(--white);
  }
  .backdrop, .bottom-band { position: absolute; left: 0; top: 0; }
  .portrait-frame { position: absolute; left: 0; top: 0; }
  .brand-box {
    position: absolute;
    left: 804px; top: 306px;
    width: 366px; height: 187px;
    background: var(--white);
    display: flex; align-items: center; justify-content: center;
    text-align: center;
  }
  .brand-name {
    font-family: "Montserrat", sans-serif;
    font-weight: 700;
    color: var(--teal);
    font-size: 34px;
    line-height: 1.15;
    letter-spacing: 0.5px;
  }
  .pill {
    position: absolute;
    left: 50px; width: 1092px; height: 293px;
    background: var(--teal);
    border-radius: 147px;
    display: flex; align-items: center; justify-content: center;
    text-align: center;
    font-weight: 600;
    font-size: 90px;
    line-height: 1.2;
  }
  .pill--service { top: 910px; }
  .pill--license { top: 2033px; font-size: 94px; }
  .program-card {
    position: absolute;
    left: 64px; top: 1259px;
    width: 1070px; height: 724px;
    background: var(--teal);
    border-radius: 240px;
  }
  .program-title {
    position: absolute;
    left: 95px; top: 125px;
    margin: 0;
    font-weight: 700;
    font-size: 92px;
    line-height: 1.2;
    letter-spacing: -0.5px;
  }
  .program-text {
    position: absolute;
    left: 97px; top: 402px;
    width: 830px;
    margin: 0;
    font-family: "Montserrat", sans-serif;
    font-weight: 500;
    font-size: 40px;
    line-height: 1.2;
    text-align: justify;
    letter-spacing: 0.5px;
  }
  .contact {
    position: absolute;
    display: flex; align-items: flex-start; gap: 22px;
  }
  .contact-icon { width: 64px; height: 64px; flex: none; }
  .contact-label {
    font-family: "Montserrat", sans-serif;
    font-weight: 700;
    font-size: 25px;
    line-height: 1.2;
    margin: 0;
  }
  .contact-value {
    font-family: "Montserrat", sans-serif;
    font-weight: 500;
    font-size: 27px;
    line-height: 1.15;
    margin: 0;
  }
  .contact--phone { left: 133px; top: 2522px; }
  .contact--email { left: 676px; top: 2592px; }
  .contact--web { left: 134px; top: 2670px; }
</style>
</head>
<body>
<main class="banner">
  <svg class="backdrop" width="1200" height="2865" viewBox="0 0 1200 2865" aria-hidden="true">
    <polygon points="0,700 1200,1500 1200,1620 0,820" fill="#ffffff" opacity="0.45"/>
    <polygon points="0,1250 1200,2050 1200,2110 0,1310" fill="#ffffff" opacity="0.4"/>
    <polygon points="300,0 1200,600 1200,700 150,0" fill="#ffffff" opacity="0.5"/>
    <polygon points="0,1900 900,2480 700,2480 0,2030" fill="#ffffff" opacity="0.35"/>
    <circle cx="1040" cy="2375" r="8" fill="#ffffff"/>
    <circle cx="1078" cy="2402" r="8" fill="#ffffff"/>
    <circle cx="1115" cy="2428" r="8" fill="#ffffff"/>
  </svg>

  <svg class="portrait-frame" width="820" height="830" viewBox="0 0 820 830">
    <defs>
      <linearGradient id="portraitTone" x1="0" y1="0" x2="0" y2="1">
        <stop offset="0" stop-color="var(--photo-top)"/>
        <stop offset="0.45" stop-color="#8a8d94"/>
        <stop offset="1" stop-color="var(--photo-bottom)"/>
      </linearGradient>
    </defs>
    <circle cx="109" cy="163" r="96" fill="var(--teal)"/>
    <circle cx="404" cy="441" r="376" fill="var(--teal)"/>
    <circle cx="707" cy="717" r="98" fill="var(--teal)"/>
    <circle cx="404" cy="441" r="336" fill="url(#portraitTone)" role="img" aria-label="Portrait photo of the brokerage's broker in a dark hat and jacket"/>
  </svg>

  <div class="brand-box">
    <div class="brand-name">Harbor Crest<br>Realty Group</div>
  </div>

  <div class="pill pill--service">A Full Service Real<br>Estate Brokerage</div>

  <section class="program-card">
    <h2 class="program-title">Home of the LIFT<br>PROGRAM</h2>
    <p class="program-text">A program that teaches, supports and celebrates Agents generating Multiple Streams of Income</p>
  </section>

  <div class="pill pill--license">Licensed in DC, MD<br>and VA</div>

  <svg class="bottom-band" width="1200" height="2865" viewBox="0 0 1200 2865" aria-hidden="true">
    <path d="M0,2480 Q600,2270 1200,2480 L1200,2865 L0,2865 Z" fill="var(--teal)"/>
  </svg>

  <div class="contact contact--phone">
    <svg class="contact-icon" viewBox="0 0 64 64" aria-hidden="true">
      <circle cx="32" cy="32" r="31" fill="var(--white)"/>
      <path d="M22 17c2-1 4 0 5 2l3 6c1 2 0 3-1 4l-2 2c1 4 5 8 9 9l2-2c1-1 2-2 4-1l6 3c2 1 3 3 2 5l-2 3c-2 2-5 3-8 2-9-3-17-11-20-20-1-3 0-6 2-8z" fill="var(--teal)"/>
    </svg>
    <div>
      <p class="contact-label">PHONE</p>
      <p class="contact-value">(301) 555-0172</p>
    </div>
  </div>

  <div class="contact contact--email">
    <svg class="contact-icon" viewBox="0 0 64 64" aria-hidden="true">
      <circle cx="32" cy="32" r="31" fill="var(--white)"/>
      <rect x="15" y="20" width="34" height="24" rx="2" fill="none" stroke="var(--teal)" stroke-width="3"/>
      <path d="M15 21l17 13 17-13M15 43l12-10M49 43l-12-10" fill="none" stroke="var(--teal)" stroke-width="3"/>
    </svg>
    <div>
      <p class="contact-label">EMAIL</p>
      <p class="contact-value">@harborcrestrealtygroup</p>
    </div>
  </div>

  <div class="contact contact--web">
    <svg class="contact-icon" viewBox="0 0 64 64" aria-hidden="true">
      <circle cx="32" cy="32" r="31" fill="var(--white)"/>
      <g fill="none" stroke="var(--teal)" stroke-width="2.5">
        <circle cx="32" cy="32" r="17"/>
        <ellipse cx="32" cy="32" rx="7" ry="17"/>
        <path d="M15 32h34M18 23h28M18 41h28M32 15v34"/>
      </g>
    </svg>
    <div>
      <p class="contact-label">WEBSITE</p>
      <p class="contact-value">www.harborcrestrealty.example<br>www.careersatharborcrest.example</p>
    </div>
  </div>
</main>
</body>
</html>
```